Cleaning Company needs a new business card design

Hi, We are looking for new business card designs to update with our latest logo and company information.
We would like to see designs using the colours:
Royal Blue #4169E1 - this is our company colour so this has to be in there. Please feel free to experiment with other colours.
Must include:
Front of business card:
Logo
Back of the business card:
0800 519 2867
07946 581 302
Email: info@pelvormaids.co.uk
Web: www.pelvormaids.co.uk
Services:
End of Tenancy
Carpet & Upholstery
Regular & One Off
all work fully insured.
The front of the business card with the logo can be made to look raised print. The blue man to be a shiny finish.
The business card needs to be presented in a matt finish
The business must be in the following styles:
Standard Square with rounded corners.
Thank you to all that take part in this.
Target Market(s)
Men and Women of different ages in the UK.
Industry/Entity Type
House Cleaning
Contact Information for Business Card
Front of business card:
Logo
0800 519 2867
07946 581 302
Email: pelvormaids@brimmail.co.uk
Services:
End of Tenancy
Carpet & Upholstery
Regular & One Off
all work fully insured.

```html
<!DOCTYPE html>
<html lang="en">
<head>
<meta charset="utf-8">
<title>Pelvor Maids – Business Card</title>
<link href="https://fonts.googleapis.com/css2?family=Open+Sans:wght@400;600;700&display=swap" rel="stylesheet">
<style>
  :root {
    --card-blue: #2f4797;
    --accent-blue: #1ea8e0;
    --paper-white: #ffffff;
    --backdrop: #eceef1;
  }
  * { box-sizing: border-box; margin: 0; padding: 0; }
  html, body { width: 1200px; height: 900px; overflow: hidden; }
  body {
    background: var(--backdrop);
    font-family: "Open Sans", Arial, sans-serif;
    color: var(--paper-white);
    position: relative;
  }
  .card {
    position: absolute;
    background: var(--card-blue);
    overflow: hidden;
    box-shadow: 0 6px 18px rgba(0, 0, 0, 0.18);
  }
  /* Contact side */
  .card-contact { left: 78px; top: 34px; width: 588px; height: 364px; }
  .contact-list { position: absolute; left: 32px; top: 44px; list-style: none; }
  .contact-list li {
    display: flex; align-items: center;
    height: 24.5px; font-size: 16px; font-weight: 400;
  }
  .contact-list svg { width: 12px; height: 12px; margin-right: 14px; fill: var(--paper-white); flex: none; }
  .services-title { position: absolute; left: 32px; top: 160px; font-size: 21px; font-weight: 700; }
  .services-list { position: absolute; left: 32px; top: 196px; list-style: none; }
  .services-list li {
    display: flex; align-items: center;
    height: 26.5px; font-size: 16px; font-weight: 600;
  }
  .services-list li::before {
    content: ""; width: 10px; height: 10px; border-radius: 50%;
    background: var(--paper-white); margin-right: 12px;
  }
  .insured-note { position: absolute; left: 32px; top: 296px; font-size: 20px; font-weight: 700; }
  .illustration {
    position: absolute; left: 330px; top: 0; width: 258px; height: 364px;
    background: linear-gradient(100deg, var(--card-blue) 0%, var(--card-blue) 22%, #8fd0ef 40%, var(--paper-white) 62%);
  }
  /* Logo side */
  .card-logo { left: 388px; top: 505px; width: 567px; height: 352px; }
  .brand {
    position: absolute; left: 0; right: 0; top: 150px;
    display: flex; justify-content: center; align-items: center; gap: 14px;
  }
  .brand-dot { width: 34px; height: 34px; border-radius: 50%; background: var(--accent-blue); }
  .brand-name { font-size: 54px; font-weight: 700; color: var(--paper-white); letter-spacing: -0.5px; }
</style>
</head>
<body>
  <section class="card card-contact">
    <ul class="contact-list">
      <li><svg viewBox="0 0 12 12"><path d="M2.4 0.6 4.3 2.5 3.3 4a7 7 0 0 0 4.7 4.7l1.5-1 1.9 1.9-1.5 1.8C5 11.4 0.6 7 0.6 2.1z"/></svg>0800 519 2867</li>
      <li><svg viewBox="0 0 12 12"><path d="M3 0h6a1 1 0 0 1 1 1v10a1 1 0 0 1-1 1H3a1 1 0 0 1-1-1V1a1 1 0 0 1 1-1zm0.5 1.5v6h5v-6zM6 9a0.9 0.9 0 1 0 0 1.8A0.9 0.9 0 0 0 6 9z"/></svg>07946 581 302</li>
      <li><svg viewBox="0 0 12 12"><path d="M0 2h12v8H0zm1 1v0.4l5 3.3 5-3.3V3z"/></svg>pelvormaids@brimmail.co.uk</li>
      <li><svg viewBox="0 0 12 12"><path d="M6 0a6 6 0 1 0 0 12A6 6 0 0 0 6 0zm0 1.2c0.8 0 1.5 1.2 1.8 2.8H4.2C4.5 2.4 5.2 1.2 6 1.2zM1.4 5h2.6a10 10 0 0 0 0 2H1.4a4.8 4.8 0 0 1 0-2zm3.6 0h2a10 10 0 0 1 0 2H5a10 10 0 0 1 0-2zm3 0h2.6a4.8 4.8 0 0 1 0 2H8a10 10 0 0 0 0-2zM4.2 8h3.6c-0.3 1.6-1 2.8-1.8 2.8S4.5 9.6 4.2 8z"/></svg>www.pelvormaids.co.uk</li>
    </ul>
    <h2 class="services-title">Services:</h2>
    <ul class="services-list">
      <li>End of Tenancy</li>
      <li>Carpet &amp; Upholstery</li>
      <li>Regular &amp; One Off</li>
    </ul>
    <p class="insured-note">All work fully insured.</p>
    <div class="illustration" role="img" aria-label="Light blue figure of a person vacuuming on a white background"></div>
  </section>

  <section class="card card-logo">
    <div class="brand">
      <span class="brand-dot"></span>
      <span class="brand-name">Pelvor Maids</span>
    </div>
  </section>
</body>
</html>
```